www.brightvalejourneys.example Weebly Web Design *with Coding*

I am looking for a fully operational Weebly design for www.brightvalejourneys.example that has the following:
1. Menus - I want the ability to have Multiple drop down menus.
2. E-commerce - The first iteration doesn't need to have e-commerce but the I might want that ability in the future.
3. Registration forms that can be filled out online. (I would give the fields that need to be filled out.)
4. Contracts that can be read and signed online that would be legally binding. (I would give the contract wording)
5. Pictures - Incorporates Professional Pictures that I have.
6. Site is offering Travel Services.
7. Logo - I already have a logo being developed elsewhere.
8. Domain Name - I already have the domain name secured and a temporary self-made site up that is built on Weebly.
9. I want to be able to take your design and do my own changes via Weebly.
10. Feel free to use any of the things you have already seen on the placeholder site I have up right now.
11. I want password protected pages that can only be accessed by a password.

Bright Vale Journey Advisors
www.brightvalejourneys.example

RE: Wire Frame

Home Page
Pictures
Short philosophy of Bright Vale Journeys
Israel Trips
March 15-27, 2019 Itinerary
Places
Hotels
Day by Day
Pictures
March 30 – April 9, 2019
Places
Hotels
Day by Day
Pictures
Europe Trips
Italy
England
Ireland
About Us
Core Values and Mission
Founders
Pilgrimage vs. Trip
FAQ’s
General Information
Flights
Hotels
Inclusions/Exclusions to Cost
Payment Plans
Forms – Password Protected
Trip Questionnaire
Trip Contract
Legal
Bottom of Page Stuff

Target Market(s)

45 - 70 year olds looking to travel on custom guided tours.

Colors

Designer to choose colors to be used in the design.

Requirements
Must have
• 1. Ability to easily update the site.
• 2. Documents that can be filled out online and feed to me.
• 3. Great Flow - easy to navigate, easy drop down menus for more trips/pages.
• 4. Pictures that draw people in and want to travel with my company.
• 5. Clean look but not sterile.

```html
<!DOCTYPE html>
<html lang="en">
<head>
<meta charset="utf-8">
<title>Bright Vale Journeys</title>
<link href="https://fonts.googleapis.com/css2?family=Work+Sans:wght@400;500;600;700;800&display=swap" rel="stylesheet">
<style>
:root{
  --ink:#2a2a2a;
  --muted:#555;
  --white:#fff;
  --card:#efefef;
  --panel:#f3f3f3;
  --btn:#262626;
  --footer:#e6e6e6;
  --line:#cfcfcf;
}
*{box-sizing:border-box;margin:0;padding:0}
html,body{width:1200px;height:2624px;overflow:hidden}
body{font-family:'Work Sans',sans-serif;color:var(--ink);background:var(--white);position:relative}
.abs{position:absolute}
.center{left:0;width:1200px;text-align:center}

.hero{top:0;left:0;width:1200px;height:560px;
  background:linear-gradient(180deg,#e9e6e0 0%,#b8a68a 8%,#8a6a48 30%,#6b4e35 60%,#4d3a2c 100%)}
.hero-shade{top:0;left:0;width:1200px;height:560px;background:linear-gradient(180deg,rgba(255,255,255,.55) 0,rgba(255,255,255,0) 90px,rgba(0,0,0,.1) 100%)}
.brand{left:133px;top:10px;font-size:23px;font-weight:500;color:var(--ink);white-space:nowrap}
.main-nav{left:440px;width:627px;top:16px;display:flex;justify-content:space-between;font-size:11px;align-items:center;white-space:nowrap}
.main-nav span{padding:2px 5px}
.main-nav .active{border:1px solid var(--ink)}
.hero-title{top:160px;font-size:62px;line-height:70px;font-weight:800;color:var(--white);letter-spacing:1px}
.hero-link{top:316px;font-size:16px;color:var(--white);letter-spacing:1px}
.arrow{top:270px}

.section-title{font-size:23px;font-weight:500;letter-spacing:1px}
.section-sub{font-size:17px}

.tile{width:299px;height:171px}
.tile-text{background:var(--panel);text-align:center;padding-top:56px}
.tile-text h3{font-size:16px;font-weight:600;letter-spacing:1px;margin-bottom:10px}
.tile-text p{font-size:11px;color:#666;line-height:17px;padding:0 44px}

.about{top:1156px;left:0;width:1200px;height:346px;background:linear-gradient(135deg,#2e3a40,#3c4747 50%,#2a3034)}
.about h2{top:112px;font-size:24px;font-weight:500;color:var(--white);letter-spacing:1px}
.about p{top:146px;left:140px;width:920px;text-align:center;font-size:14.5px;line-height:26px;color:#e8e8e8}

.card{top:1662px;width:222px;height:279px;background:var(--card);text-align:center}
.card .photo{margin:3px;height:156px}
.card h4{font-size:17px;font-weight:400;margin-top:16px}
.card .price{font-size:13px;margin-top:4px}
.btn{display:inline-block;background:var(--btn);color:var(--white);font-size:11px;letter-spacing:.5px;width:138px;height:34px;line-height:34px;margin-top:10px;text-align:center}

.promo{top:2020px;left:0;width:1200px;height:347px;background:linear-gradient(90deg,#3a4250 0%,#3c4451 55%,#4a4b50 80%,#3a3f48 100%)}
.promo .btn{position:absolute;left:530px;top:117px;width:140px;background:#555a60;margin:0}
.promo h2{top:178px;font-size:24px;font-weight:500;color:var(--white);letter-spacing:1px}
.promo p{top:220px;font-size:17px;color:#d8d8d8;letter-spacing:.5px}

.foot-nav{top:2404px;display:flex;justify-content:center;gap:34px;font-size:10.5px;color:#666;letter-spacing:.5px}
.footer{top:2457px;left:0;width:1200px;height:167px;background:var(--footer)}
.info{top:30px;font-size:11px}
.info b{display:block;font-size:12px;font-weight:600;letter-spacing:.5px;margin-bottom:6px}
.info span{font-size:10px;color:#555}
.divider{left:133px;top:91px;width:934px;height:1px;background:var(--line)}
.copy{top:118px;font-size:10px;color:#555}
.social{top:30px;left:918px;display:flex;gap:12px}
.social i{display:block;width:28px;height:28px;border-radius:50%;background:#555}
</style>
</head>
<body>

<header>
  <div class="abs hero" role="img" aria-label="Aerial photograph of a historic city square with a colonnade at sunset"></div>
  <div class="abs hero-shade"></div>
  <div class="abs brand">Bright Vale Journeys</div>
  <nav class="abs main-nav">
    <span class="active">Home</span>
    <span>Overview and Hotels</span>
    <span>2019 - March 15-28 Israel/Petra</span>
    <span>Trip Sign Up</span>
    <span>General Trip Information</span>
    <span>More</span>
  </nav>
  <h1 class="abs center hero-title">TRAVEL.&nbsp; LIFE.<br>BRIGHT VALE.</h1>
  <div class="abs center hero-link">READ MORE</div>
  <svg class="abs arrow" style="left:4px" width="20" height="20" viewBox="0 0 20 20"><path d="M16 10H5M9 5l-5 5 5 5" stroke="#fff" stroke-width="2.5" fill="none"/></svg>
  <svg class="abs arrow" style="left:1176px" width="20" height="20" viewBox="0 0 20 20"><path d="M4 10h11M11 5l5 5-5 5" stroke="#fff" stroke-width="2.5" fill="none"/></svg>
</header>

<section>
  <h2 class="abs center section-title" style="top:633px">WE HAVE LED GROUPS ALL OVER THE WORLD</h2>
  <p class="abs center section-sub" style="top:668px">Including trips throughout</p>
  <div class="abs tile" style="left:133px;top:712px;background:linear-gradient(180deg,#d98a2a,#b4501a 60%,#3a1e10)" role="img" aria-label="Domed mosque with minarets at sunset"></div>
  <div class="abs tile" style="left:451px;top:712px;background:linear-gradient(180deg,#6aa0d8,#a9c3dc 45%,#6c7684 75%,#3d4c5e)" role="img" aria-label="River bridge and city skyline under a blue sky"></div>
  <div class="abs tile" style="left:768px;top:712px;background:linear-gradient(160deg,#2b7fa8,#48a2c0 45%,#b0a58e 70%,#6f6a5e)" role="img" aria-label="Coastal city seen from above with turquoise sea"></div>
  <div class="abs tile" style="left:133px;top:904px;background:linear-gradient(180deg,#e3842e,#c8642a 40%,#8a6a5a 70%,#3c5a3a)" role="img" aria-label="Ornate temple complex at sunset"></div>
  <div class="abs tile tile-text" style="left:451px;top:904px">
    <h3>MAURIS BIBENDUM</h3>
    <p>Nulla in lorem at massa pellentesque posuere. Nulla tristique posuere</p>
  </div>
  <div class="abs tile" style="left:768px;top:904px;background:linear-gradient(180deg,#4a8ac8,#7aa4c8 40%,#b2863a 70%,#6a4a2a)" role="img" aria-label="Row of golden seated statues before a blue temple roof"></div>
</section>

<section class="abs about" role="img" aria-label="Dim view over a coastal city with a hilltop statue">
  <h2 class="abs center">ABOUT US</h2>
  <p class="abs">Duis ornare erat eget magna dapibus, in accumsan quam pharetra. Nam tempus, quam in bibendum vulputate, sapien dolor viverra nisl, vitae euismod elit turpis et nulla. Aliquam erat volutpat. Pellentesque blandit lacus eget nunc faucibus, et tincidunt eros viverra. Phasellus consequat sagittis nisi suscipit feugiat. Cras eget leo sed nunc hendrerit ultricies eu at nisl.</p>
</section>

<section>
  <h2 class="abs center section-title" style="top:1578px">FEATURED TOURS</h2>
  <p class="abs center section-sub" style="top:1616px">Aliquam consectetur orci</p>
  <div class="abs card" style="left:133px">
    <div class="photo" role="img" aria-label="Stone statues on a colonnade under blue sky" style="background:linear-gradient(180deg,#2d5aa8,#8ea6c8 50%,#9b948a)"></div>
    <h4>Proin eget</h4><div class="price">$1,500</div><span class="btn">BOOK NOW</span>
  </div>
  <div class="abs card" style="left:370px">
    <div class="photo" role="img" aria-label="Traveller with a backpack in a colourful park" style="background:linear-gradient(180deg,#6a9ad8,#a9bfd4 40%,#7a7a5a 70%,#6a5040)"></div>
    <h4>Sed augue</h4><div class="price">$1,000</div><span class="btn">BOOK NOW</span>
  </div>
  <div class="abs card" style="left:607px">
    <div class="photo" role="img" aria-label="Golden temple under a purple evening sky" style="background:linear-gradient(180deg,#5a4aa8,#c85a8a 40%,#c87a3a 70%,#8a3a1a)"></div>
    <h4>Aliquam</h4><div class="price">$1,200</div><span class="btn">BOOK NOW</span>
  </div>
  <div class="abs card" style="left:844px">
    <div class="photo" role="img" aria-label="Old city walls and a golden dome at dusk" style="background:linear-gradient(180deg,#d88ab8,#c8a0c8 40%,#9a8aa0 60%,#4a4a5a)"></div>
    <h4>Vestibulum</h4><div class="price">$1,350</div><span class="btn">BOOK NOW</span>
  </div>
</section>

<section class="abs promo" role="img" aria-label="Large bronze seated statue against an overcast sky">
  <span class="btn">BOOK NOW</span>
  <h2 class="abs center">FUSCE SOLLICITUDIN ET LUCTUS VOLUTPAT</h2>
  <p class="abs center">Proin placerat dapibus gravida</p>
</section>

<nav class="abs center foot-nav">
  <span>HOME</span><span>OVERVIEW AND HOTELS</span><span>2019 - MARCH 15-28 ISRAEL/PETRA</span><span>TRIP SIGN UP</span><span>GENERAL TRIP INFORMATION</span><span>MORE</span>
</nav>

<footer class="abs footer">
  <div class="abs info" style="left:133px"><b>HOURS</b><span>M-F: 7am - 9pm</span></div>
  <div class="abs info" style="left:237px"><b>TELEPHONE</b><span>555 010 2468</span></div>
  <div class="abs info" style="left:349px"><b>EMAIL</b><span>info@brightvalejourneys.example</span></div>
  <div class="abs social"><i></i><i></i><i></i><i></i></div>
  <div class="abs divider"></div>
  <div class="abs center copy">Copyright &nbsp;©&nbsp; 2018 Bright Vale Journeys.&nbsp; All rights reserved.</div>
</footer>

</body>
</html>
```